Silver Brook Custom Homes business card. Double sided. Modern. professional

Silver Brook Custom Homes
contemporary modern design with our logo /
Double sided with all our contact information
Use same Green colors as in our Logo. Contemporary logo that grabs your attention. Visually pleasing and balanced. Easy to read, and Vibrant. Would love an option for rounded edges. Embossed logo would be amazing.
Contact Information for Business Card
Dana Pellman Owner / General Contractor Silver Brook Custom Homes p: 803.555.0142 m: 865.555.0178 e: silverbrookcustomhomes@mailnest.example w: www.silverbrookcustomhomes.example 218 Wrenfield Mill Road Batesburg, SC 29088

```html
<!DOCTYPE html>
<html lang="en">
<head>
<meta charset="utf-8">
<title>Silver Brook Custom Homes – Business Card</title>
<link href="https://fonts.googleapis.com/css2?family=Cinzel:wght@500&family=Open+Sans:wght@400;600&display=swap" rel="stylesheet">
<style>
  :root {
    --stage: #d6d6d6;
    --paper: #ffffff;
    --green: #5b7a35;
    --green-dark: #3d5620;
    --green-light: #8cc43f;
    --ink: #333333;
    --rule: #6f8f3f;
  }
  * { box-sizing: border-box; margin: 0; padding: 0; }
  html, body { width: 1200px; height: 800px; overflow: hidden; }
  body {
    background: var(--stage);
    display: flex;
    align-items: center;
    justify-content: center;
    gap: 40px;
    font-family: "Open Sans", Arial, sans-serif;
    color: var(--ink);
  }
  .card {
    position: relative;
    width: 540px;
    height: 308px;
    border-radius: 12px;
    overflow: hidden;
    box-shadow: 0 6px 18px rgba(0,0,0,.18);
  }

  /* Front */
  .card--front { background: var(--paper); }
  .brand {
    position: absolute;
    top: 42px; right: 30px;
    display: flex; align-items: center; gap: 12px;
  }
  .brand__dot {
    width: 36px; height: 36px; border-radius: 50%;
    background: var(--green);
  }
  .brand__name {
    font-family: "Open Sans", Arial, sans-serif;
    font-weight: 600;
    font-size: 26px;
    color: var(--green);
  }
  .person {
    position: absolute;
    left: 30px; top: 118px;
  }
  .person__name {
    font-family: "Cinzel", Georgia, serif;
    font-weight: 500;
    font-size: 22px;
    letter-spacing: 1px;
    color: var(--green);
    line-height: 1.1;
  }
  .person__title { font-size: 13px; color: var(--ink); }
  .divider {
    position: absolute;
    left: 30px; right: 30px; top: 178px;
    height: 1px; background: var(--rule);
  }
  .contacts {
    position: absolute;
    left: 30px; bottom: 26px;
    list-style: none;
    font-size: 11.5px;
    line-height: 1.2;
  }
  .contacts li { display: flex; align-items: center; gap: 6px; margin-top: 5px; }
  .contacts .web { color: var(--green); font-weight: 600; }
  .icon { width: 16px; height: 16px; flex: none; }
  .address {
    position: absolute;
    right: 30px; top: 192px;
    text-align: right;
    font-size: 12.5px;
    line-height: 1.4;
    font-style: normal;
  }
  .address__company { color: var(--green); font-weight: 600; }

  /* Back */
  .card--back { background: var(--green); }
  .pattern {
    position: absolute; inset: 0;
    background: linear-gradient(200deg, var(--green-light) 0%, var(--green) 45%, var(--green-dark) 100%);
  }
  .back-brand {
    position: absolute; inset: 0;
    display: flex; flex-direction: column; align-items: center; justify-content: center; gap: 14px;
  }
  .back-brand__dot { width: 40px; height: 40px; border-radius: 50%; background: var(--paper); }
  .back-brand__name {
    font-family: "Open Sans", Arial, sans-serif;
    font-weight: 600;
    font-size: 28px;
    color: var(--paper);
  }
</style>
</head>
<body>

<section class="card card--front">
  <div class="brand">
    <span class="brand__dot"></span>
    <span class="brand__name">Silver Brook</span>
  </div>

  <div class="person">
    <h1 class="person__name">DANA PELLMAN</h1>
    <p class="person__title">Owner / General Contractor</p>
  </div>

  <div class="divider"></div>

  <ul class="contacts">
    <li>
      <svg class="icon" viewBox="0 0 16 16"><circle cx="8" cy="8" r="8" fill="#5b7a35"/><path d="M5 4.5c.6-.4 1.1 0 1.4.6l.4.9c.2.4 0 .8-.3 1l-.4.3c.4.9 1 1.6 1.9 2l.3-.4c.3-.3.7-.4 1-.2l.9.5c.6.3.8.9.4 1.4-.6.8-1.6 1-2.6.4C6.4 10 5.4 8.8 4.8 7.3c-.4-1.1-.3-2.2.2-2.8z" fill="#fff"/></svg>
      <span>803.555.0142</span>
      <svg class="icon" viewBox="0 0 16 16"><circle cx="8" cy="8" r="8" fill="#5b7a35"/><rect x="5.3" y="3.5" width="5.4" height="9" rx="1" fill="none" stroke="#fff" stroke-width="1.2"/><circle cx="8" cy="11" r=".6" fill="#fff"/></svg>
      <span>865.555.0178</span>
    </li>
    <li>
      <svg class="icon" viewBox="0 0 16 16"><circle cx="8" cy="8" r="8" fill="#5b7a35"/><rect x="4" y="5" width="8" height="6" fill="none" stroke="#fff" stroke-width="1.1"/><path d="M4 5l4 3.3L12 5" fill="none" stroke="#fff" stroke-width="1.1"/></svg>
      <span>silverbrookcustomhomes@mailnest.example</span>
    </li>
    <li>
      <svg class="icon" viewBox="0 0 16 16"><circle cx="8" cy="8" r="8" fill="#5b7a35"/><circle cx="8" cy="8" r="4.3" fill="none" stroke="#fff" stroke-width="1"/><ellipse cx="8" cy="8" rx="1.8" ry="4.3" fill="none" stroke="#fff" stroke-width="1"/><path d="M3.7 8h8.6" stroke="#fff" stroke-width="1"/></svg>
      <span class="web">www.silverbrookcustomhomes.example</span>
    </li>
  </ul>

  <address class="address">
    <div class="address__company">Silver Brook Custom Homes</div>
    <div>218 Wrenfield Mill Road</div>
    <div>Batesburg, SC 29088</div>
  </address>
</section>

<section class="card card--back">
  <div class="pattern" role="img" aria-label="Repeating embossed brand pattern in light-to-dark green"></div>
  <div class="back-brand">
    <span class="back-brand__dot"></span>
    <span class="back-brand__name">Silver Brook</span>
  </div>
</section>

</body>
</html>
```